Stationary Set Rebrand for Brenvik

We are a Canadian Distribution and Service Company that was established in 1969. Over the past 5 decades we have expanded our business and have warehouses across Canada. We specialize in adhesive tapes, adhesives, films, safety, warehouse, shipping, janitorial and packaging supplies.

We have updated our logo design and would like a new corporate branding identity that includes a new fresh Stationary Set (Business Cards, Letterhead, Letterhead MS Word, Envelope, Presentation Folders, Email Signatures, Notepad Covers, etc.)

Target Market(s)

Industrial Business Sector

Font styles to use
Sans Serif

Colors
0054AA
0677BA
7BADD7
CADEEF
E8F1F8
0094D4
00A9DD
6FCCEA
C7EBF8
E9F6FB
00AB8E
00BBA5
67D7C9
C6EFE9
E9F9F6
EB3D1F
EC4F4E
F09395
F8D3D4
FCEDEE

Requirements
Should not have
• Colors not too light, darker colours preferred

```html
<!DOCTYPE html>
<html lang="en">
<head>
<meta charset="utf-8">
<title>Brenvik Presentation Folder</title>
<link href="https://fonts.googleapis.com/css2?family=Roboto:wght@400;700;900&display=swap" rel="stylesheet">
<style>
  :root {
    --backdrop: #d9d9db;
    --folder-red: #c8111b;
    --folder-red-deep: #8e0a12;
    --motif-red: #7a0810;
    --paper-white: #ffffff;
    --paper-shade: #ececec;
    --ink: #1d1d1d;
    --ink-muted: #4a4a4a;
    --accent-red: #d0141f;
  }
  * { margin: 0; padding: 0; box-sizing: border-box; }
  html, body {
    width: 1200px;
    height: 847px;
    overflow: hidden;
    background: var(--backdrop);
    font-family: "Roboto", Arial, sans-serif;
  }
  .folder-spread {
    position: absolute;
    left: 70px;
    top: 52px;
    width: 1060px;
    height: 743px;
    display: flex;
    box-shadow: 0 18px 40px rgba(0,0,0,0.25);
  }
  .panel {
    position: relative;
    width: 530px;
    height: 100%;
  }
  /* Back cover */
  .panel--back {
    background: linear-gradient(90deg, var(--folder-red) 0%, var(--folder-red) 70%, var(--folder-red-deep) 100%);
  }
  .leaf-motif {
    position: absolute;
    left: 95px;
    top: 150px;
    width: 330px;
    height: 290px;
    border-radius: 50%;
    background: radial-gradient(ellipse at 50% 55%, var(--motif-red) 0%, #9a0b14 55%, rgba(200,17,27,0) 75%);
  }
  .contact-block {
    position: absolute;
    left: 0;
    right: 0;
    bottom: 105px;
    text-align: center;
    color: var(--paper-white);
    font-size: 11.5px;
    line-height: 1.45;
    letter-spacing: 0.3px;
  }
  .contact-line { display: flex; justify-content: center; align-items: center; gap: 5px; }
  .contact-icon { width: 11px; height: 11px; fill: var(--paper-white); }
  /* Front cover */
  .panel--front {
    background: linear-gradient(100deg, var(--paper-white) 0%, var(--paper-white) 45%, var(--paper-shade) 100%);
  }
  .brand-lockup {
    position: absolute;
    left: 88px;
    top: 300px;
  }
  .brand-name {
    display: flex;
    align-items: center;
    gap: 12px;
    font-weight: 900;
    font-size: 64px;
    line-height: 1;
    color: var(--ink);
    letter-spacing: -1px;
  }
  .brand-mark {
    width: 16px;
    height: 16px;
    background: var(--accent-red);
    margin-top: 28px;
  }
  .brand-tagline {
    margin-top: 6px;
    font-weight: 700;
    font-size: 14px;
    color: var(--ink);
    letter-spacing: 0.6px;
  }
  .front-web {
    position: absolute;
    left: 0;
    right: 0;
    bottom: 50px;
    text-align: center;
    font-size: 12px;
    letter-spacing: 2px;
    color: var(--ink-muted);
  }
  .front-web span { color: var(--accent-red); }
</style>
</head>
<body>
  <main class="folder-spread">
    <section class="panel panel--back">
      <div class="leaf-motif" role="img" aria-label="Large embossed decorative leaf motif"></div>
      <div class="contact-block">
        <p>48 Alder Ridge Road, Markham, ON L3R 5K2</p>
        <p class="contact-line">
          <svg class="contact-icon" viewBox="0 0 24 24" aria-hidden="true"><path d="M6.6 10.8a15.1 15.1 0 0 0 6.6 6.6l2.2-2.2a1 1 0 0 1 1-.25 11.4 11.4 0 0 0 3.6.57 1 1 0 0 1 1 1V20a1 1 0 0 1-1 1A17 17 0 0 1 3 4a1 1 0 0 1 1-1h3.5a1 1 0 0 1 1 1c0 1.25.2 2.45.57 3.6a1 1 0 0 1-.25 1z"/></svg>
          (905) 555-0148
          <svg class="contact-icon" viewBox="0 0 24 24" aria-hidden="true"><path d="M2 5h20v14H2zm2 2v.5l8 5 8-5V7zm0 2.9V17h16V9.9l-8 5z"/></svg>
          info@brenvik-supply.ca
        </p>
        <p>www.brenvik-supply.ca</p>
      </div>
    </section>
    <section class="panel panel--front">
      <div class="brand-lockup">
        <div class="brand-name">Brenvik<span class="brand-mark" aria-hidden="true"></span></div>
        <p class="brand-tagline">Tape and Packaging Specialists</p>
      </div>
      <p class="front-web">www.<span>brenvik-supply</span>.ca</p>
    </section>
  </main>
</body>
</html>
```